Harborline Estates Business Card for Apartment Buildings

Create business cards for resident managers who run apartment buildings. The audience is the public who are searching for apartment rentals, and current residents who live at the apartment building. Key design element will be incorporating the company logo, however, the logo cannot dominate. The building name and manager name are more important than the logo. Current business card design leaves little room for copy, so we may need to reduce the size on the current card to allow for more space for copy.

Target Market(s)

Adults 18-65 years of age, who are looking for an apartment rental, plus current residents who live at our apartment buildings.

Industry/Entity Type

Property Management

Contact Information for Business Card

A major design element will be use of the company logo. Important property and manager contact information must be part of the design. The size of the logo will need to be reduced to make room for building and manager contact copy.

Font styles to use
Sans Serif

Colors
3176b5
000000
959595
ffffff

Requirements
Must have
• 1) Incorporate the company logo.
• 2) Use the company colors (dark blue, black/grey, over white).
• 3) FEATURE THE BUILDING NAME
• 4) FEATURE THE MANAGER NAME
• 5) The company name is less important than BUILDING and MANAGER
• 6) Manager contact information
• **SEE ATTACHED CREATIVE BRIEF**
Nice to have
• 1) Back of card logo watermark
• 2) Ability to write notes on back of carfd
Should not have
• Avoid letting the company logo dominate the card, the building name and manager are more important than the company logo.

```html
<!DOCTYPE html>
<html lang="en">
<head>
<meta charset="utf-8">
<title>Harborline Estates Business Card</title>
<link href="https://fonts.googleapis.com/css2?family=Arimo:wght@400;700&display=swap" rel="stylesheet">
<style>
  :root {
    --brand-blue: #236db0;
    --paper: #ffffff;
    --backdrop: #f3f2f3;
    --watermark: #dfe6ee;
  }
  * { margin: 0; padding: 0; box-sizing: border-box; }
  html, body {
    width: 1014px;
    height: 1200px;
    overflow: hidden;
    background: var(--backdrop);
    font-family: "Arimo", Arial, sans-serif;
  }
  .card-spread {
    position: absolute;
    top: 202px;
    left: 146px;
    display: flex;
    gap: 58px;
  }
  .card {
    position: relative;
    width: 338px;
    height: 194px;
    overflow: hidden;
    box-shadow: 0 14px 16px -10px rgba(0,0,0,0.35);
  }
  .card-shape {
    position: absolute;
    inset: 0;
    width: 100%;
    height: 100%;
  }
  /* Front */
  .card-front { background: var(--brand-blue); }
  .front-wordmark {
    position: absolute;
    left: 10px;
    top: 78px;
    width: 116px;
    color: var(--paper);
    font-weight: 700;
    line-height: 1;
  }
  .front-wordmark .name-main { display: block; font-size: 16px; letter-spacing: -0.1px; white-space: nowrap; }
  .front-wordmark .name-sub { display: block; font-size: 8px; letter-spacing: 3.9px; margin-top: 3px; white-space: nowrap; }
  .watermark-dot {
    position: absolute;
    right: 4px;
    bottom: 4px;
    width: 36px;
    height: 36px;
    border-radius: 50%;
    border: 2px solid var(--watermark);
  }
  /* Back */
  .card-back { background: var(--paper); }
  .back-brand {
    position: absolute;
    left: 15px;
    top: 78px;
    width: 104px;
    text-align: center;
    color: var(--brand-blue);
    font-weight: 700;
    line-height: 1;
  }
  .brand-dot {
    display: block;
    width: 20px;
    height: 20px;
    margin: 0 auto 6px;
    border-radius: 50%;
    background: var(--brand-blue);
  }
  .back-brand .name-main { display: block; font-size: 14.5px; letter-spacing: -0.2px; white-space: nowrap; }
  .back-brand .name-sub { display: block; font-size: 7px; letter-spacing: 3px; margin-top: 3px; white-space: nowrap; }
  .manager {
    position: absolute;
    left: 154px;
    top: 50px;
    color: var(--paper);
  }
  .manager-name { font-size: 17px; font-weight: 700; letter-spacing: -0.2px; line-height: 1.05; white-space: nowrap; }
  .manager-title { font-size: 13.5px; font-weight: 400; margin-top: 2px; }
  .contact {
    position: absolute;
    left: 174px;
    top: 106px;
    color: var(--paper);
    font-size: 7.6px;
    line-height: 10.4px;
    white-space: nowrap;
  }
  .contact address { font-style: normal; margin-bottom: 4px; }
</style>
</head>
<body>
  <main class="card-spread">
    <section class="card card-front" aria-label="Card front">
      <svg class="card-shape" viewBox="0 0 422 243" preserveAspectRatio="none" aria-hidden="true">
        <path d="M250,0 C190,45 150,140 149,243 L422,243 L422,0 Z" fill="#ffffff"/>
      </svg>
      <div class="front-wordmark">
        <span class="name-main">HARBORLINE</span>
        <span class="name-sub">ESTATES LLC</span>
      </div>
      <span class="watermark-dot" aria-hidden="true"></span>
    </section>

    <section class="card card-back" aria-label="Card back">
      <svg class="card-shape" viewBox="0 0 422 243" preserveAspectRatio="none" aria-hidden="true">
        <path d="M65,0 C150,45 205,140 210,243 L422,243 L422,0 Z" fill="#236db0"/>
      </svg>
      <div class="back-brand">
        <span class="brand-dot" aria-hidden="true"></span>
        <span class="name-main">HARBORLINE</span>
        <span class="name-sub">ESTATES LLC</span>
      </div>
      <div class="manager">
        <div class="manager-name">DANIEL WHITFORD</div>
        <div class="manager-title">Property Manager</div>
      </div>
      <div class="contact">
        <address>2750 Ridgeway Avenue #B210<br>Portland, OR 97205</address>
        <div>Phone 503-555-0142</div>
        <div>Fax 503-555-0178</div>
        <div>daniel@harborlineestates.us</div>
        <div>www.harborlineestates.us</div>
      </div>
    </section>
  </main>
</body>
</html>
```